Harborline Talent IT Recruiting firm needs a business card design for Recruiters, Sourcers, and Account

We need business cards that allow us to change all contact info, names, titles (Recruiter, Sourcer, Account Manager, Director, CEO, etc) per person since we have three offices, in three cities, Phoenix, Austin, and Las Vegas. We do recruiting and contractors for IT positions (Developers, Architects, Software Engineers, Security Engineers, Help Desk, DBAs, PMs, Scrum Masters, etc.) Our client companies are very diverse from Crestline 250 to silicone Valley type start-ups.

So, while we what hip, techie, and quirky, it still needs to be professional. Primary color we use is blue, with silver as a secondary color.

Target Market(s)

IT, Technology

Industry/Entity Type

Business

Contact Information for Business Card

Company name: Harborline Talent, Inc.
Website: www.harborlinetalent-example.com
Logos for ProCircle, Quillo, and Roomwall

Name, Title, Office Number, Cell Number, email

Font styles to use
Serif
Sans Serif

Colors
0455a3
d5d5d5

Requirements
Nice to have
• The grey I selected below is not necessary - but, would like silver included. I included a card design (File 3: HTI early trial example.jpg) that I had started on. It's very rough, and not quite what we're looking for, but what we did like is the logo, big, maybe a bit faded, off center, goes out of frame, etc. Still looking for other ideas - you are the pros! But, just an idea of a design element we liked.

```html
<!DOCTYPE html>
<html lang="en">
<head>
<meta charset="utf-8">
<title>Harborline Talent – Business Card</title>
<link rel="stylesheet" href="https://fonts.googleapis.com/css2?family=Open+Sans:wght@300;400;700&family=Josefin+Sans:wght@300&family=Cinzel:wght@400&display=swap">
<style>
  :root {
    --brand-blue: #0455a3;
    --brand-blue-light: #1f8fc9;
    --brand-sky: #3bb3e6;
    --silver: #d5d5d5;
    --silver-light: #f2f2f2;
    --ink: #2e2e2e;
    --ink-soft: #4a5563;
    --icon-grey: #6b6b6b;
    --canvas-bg: #e9e9e9;
  }
  * { box-sizing: border-box; margin: 0; padding: 0; }
  html, body {
    width: 1200px; height: 1023px; overflow: hidden;
    background: var(--canvas-bg);
  }
  .canvas { position: relative; width: 1200px; height: 1023px; }

  .card {
    position: absolute; width: 640px; height: 366px; overflow: hidden;
    box-shadow: 0 6px 18px rgba(0,0,0,.18);
  }

  /* ---------- Front ---------- */
  .card-front { left: 60px; top: 80px; background: #fafafa; }
  .card-front .bands { position: absolute; inset: 0; }

  .logo { position: absolute; display: flex; align-items: center; gap: 10px; }
  .logo-name {
    font-family: "Josefin Sans", sans-serif; font-weight: 300;
    color: var(--ink); white-space: nowrap;
  }
  .logo-dot { border-radius: 50%; background: var(--brand-sky); flex: none; }
  .tagline {
    position: absolute; font-family: "Cinzel", serif; color: var(--ink-soft);
    letter-spacing: 2px; white-space: nowrap;
  }

  .card-front .logo { right: 40px; top: 48px; }
  .card-front .logo-name { font-size: 34px; }
  .card-front .logo-dot { width: 30px; height: 30px; }
  .card-front .tagline { right: 48px; top: 96px; font-size: 11px; }

  .company-line {
    position: absolute; font-family: "Open Sans", sans-serif; font-weight: 400;
    color: var(--ink); white-space: nowrap;
  }
  .card-front .company-line { right: 40px; top: 160px; font-size: 24px; }

  .person { position: absolute; left: 58px; top: 150px; font-family: "Open Sans", sans-serif; }
  .person-name { font-size: 22px; font-weight: 700; color: var(--brand-blue); line-height: 1.1; }
  .person-title { font-size: 14px; color: var(--ink); }

  .contact-list { position: absolute; left: 80px; top: 210px; list-style: none; font-family: "Open Sans", sans-serif; }
  .contact-list li {
    display: flex; align-items: center; gap: 10px;
    font-size: 13px; line-height: 20px; color: var(--brand-blue-light);
  }
  .contact-icon {
    width: 13px; height: 13px; border-radius: 2px; background: var(--icon-grey);
    display: inline-flex; align-items: center; justify-content: center; flex: none;
  }

  /* ---------- Back ---------- */
  .card-back {
    left: 500px; top: 560px;
    background: linear-gradient(135deg, var(--silver-light) 0%, #e3e3e3 55%, var(--silver) 100%);
  }
  .card-back .watermark-circle {
    position: absolute; left: 90px; top: 40px; width: 300px; height: 300px; border-radius: 50%;
    background: radial-gradient(circle, rgba(170,190,215,.45) 0%, rgba(190,205,225,.25) 70%, rgba(200,210,225,0) 100%);
  }
  .card-back .logo { left: 60px; top: 70px; }
  .card-back .logo-name { font-size: 52px; }
  .card-back .logo-dot { width: 44px; height: 44px; }
  .card-back .rule {
    position: absolute; left: 60px; top: 170px; width: 500px; height: 1px; background: var(--brand-blue-light);
  }
  .card-back .tagline { left: 62px; top: 144px; font-size: 16px; letter-spacing: 3px; }
  .card-back .company-line { left: 60px; top: 188px; font-size: 38px; }
</style>
</head>
<body>
<main class="canvas">

  <section class="card card-front" aria-label="Business card front">
    <svg class="bands" width="640" height="366" viewBox="0 0 640 366" aria-hidden="true">
      <defs>
        <linearGradient id="bandBlue" x1="0" y1="0" x2="1" y2="1">
          <stop offset="0" stop-color="#2a8cc4"/>
          <stop offset="1" stop-color="#0455a3"/>
        </linearGradient>
      </defs>
      <polygon points="0,0 28,0 28,366 0,366" fill="url(#bandBlue)"/>
      <polygon points="330,366 640,196 640,236 400,366" fill="url(#bandBlue)"/>
      <polygon points="400,366 640,236 640,366" fill="#0a4f8f"/>
    </svg>

    <div class="logo">
      <span class="logo-name">Harborline Talent</span>
      <span class="logo-dot"></span>
    </div>
    <p class="tagline">Meeting Every Tech Need</p>
    <p class="company-line">Harborline Talent, Inc</p>

    <div class="person">
      <p class="person-name">Dana Whitfield</p>
      <p class="person-title">Manager</p>
    </div>

    <ul class="contact-list">
      <li><span class="contact-icon">
        <svg width="9" height="9" viewBox="0 0 24 24" aria-hidden="true"><path fill="#fff" d="M6.6 10.8a15 15 0 0 0 6.6 6.6l2.2-2.2c.3-.3.7-.4 1-.2 1.1.4 2.3.6 3.6.6.6 0 1 .4 1 1V20c0 .6-.4 1-1 1A17 17 0 0 1 3 4c0-.6.4-1 1-1h3.5c.6 0 1 .4 1 1 0 1.3.2 2.5.6 3.6.1.3 0 .7-.2 1z"/></svg>
      </span>00 4718-2095</li>
      <li><span class="contact-icon"></span>03 561 204 873</li>
      <li><span class="contact-icon"></span>www.quillo-example.com</li>
      <li><span class="contact-icon"></span>www.roomwall-example.com</li>
      <li><span class="contact-icon"></span>dwhitfield@harborlinetalent-example.com</li>
      <li><span class="contact-icon"></span>www.harborlinetalent-example.com</li>
    </ul>
  </section>

  <section class="card card-back" aria-label="Business card back">
    <div class="watermark-circle"></div>
    <div class="logo">
      <span class="logo-name">Harborline Talent</span>
      <span class="logo-dot"></span>
    </div>
    <p class="tagline">Meeting Every Tech Need</p>
    <div class="rule"></div>
    <p class="company-line">Harborline Talent, Inc</p>
  </section>

</main>
</body>
</html>
```